Bref créative
Stationery for bright harbor company
Stationery for my company
Professional
Farhan Tariq Baloch
General Manager
Prince Faisal Street,
Al Warood,
Riyadh,
Saudi Arabia.
P.O.Box:5831-6-40921-3158.
farhan@br1ghth4rb0r.example
www.br1ghth4rb0r.example
C.R.
I want something creative, plus if it is possible can you put the information editable so I can put the other names and titles for the other co - workers
My logo or something creative
logo to be used
like this

```html
<!DOCTYPE html>
<html lang="en">
<head>
<meta charset="utf-8">
<title>Bright Harbor Company Stationery</title>
<link href="https://fonts.googleapis.com/css2?family=Open+Sans:wght@400;600;700&display=swap" rel="stylesheet">
<style>
  :root {
    --backdrop: #e9e4dc;
    --paper: #ffffff;
    --paper-shade: #f1f3f4;
    --brand-blue: #1f5f80;
    --brand-deep: #0f3f5c;
    --brand-light: #6fa3bf;
    --ink: #2c3a44;
    --envelope-grey: #8e9398;
    --flap: #c9cdd0;
  }
  html, body { margin: 0; padding: 0; overflow: hidden; }
  body { width: 1200px; height: 326px; background: var(--backdrop); }
  .stationery-set { display: block; width: 1200px; height: 326px; font-family: "Open Sans", sans-serif; }
  .sheet { fill: var(--paper); filter: drop-shadow(0 1px 2px rgba(0,0,0,.25)); }
  .sheet-deep { fill: var(--brand-deep); filter: drop-shadow(0 1px 2px rgba(0,0,0,.25)); }
  .wave-band { fill: var(--brand-blue); }
  .wave-line { fill: none; stroke: var(--brand-light); stroke-width: 1.2; }
  .brand-mark { fill: var(--brand-blue); }
  .brand-name { fill: var(--brand-deep); font-weight: 700; }
  .brand-name-light { fill: var(--paper); font-weight: 700; }
  .contact { fill: var(--ink); font-size: 3px; }
  .contact-right { fill: var(--ink); font-size: 2.6px; text-anchor: end; }
  .faint-mark { fill: none; stroke: var(--paper-shade); stroke-width: 6; }
  .envelope-grey { fill: var(--envelope-grey); }
  .flap-line { fill: none; stroke: var(--flap); stroke-width: 1; }
</style>
</head>
<body>
<svg class="stationery-set" viewBox="0 0 1200 326" xmlns="http://www.w3.org/2000/svg">

  <!-- Business card: front -->
  <g class="business-card card-front">
    <rect class="sheet" x="12" y="43" width="80" height="52"/>
    <circle class="brand-mark" cx="21" cy="69" r="3.5"/>
    <text class="brand-name" x="27" y="70.5" font-size="4.6">bright harbor company</text>
  </g>

  <!-- Business card: contact side -->
  <g class="business-card card-contact">
    <rect class="sheet" x="12" y="139" width="80" height="56"/>
    <rect x="14" y="142" width="22" height="50" fill="#cfd5da" role="img" aria-label="Soft grey profile illustration area"/>
    <circle class="brand-mark" cx="42" cy="148" r="2.3"/>
    <text class="brand-name" x="46" y="149.3" font-size="3.4">bright harbor company</text>
    <text class="contact" x="40" y="160" font-weight="700">Contact Name</text>
    <text class="contact" x="40" y="164">Position Title</text>
    <text class="contact" x="40" y="171">Street Name, District</text>
    <text class="contact" x="40" y="175">City, Country</text>
    <text class="contact" x="40" y="179">Email Address</text>
    <text class="contact" x="40" y="183">Web Address</text>
  </g>

  <!-- Business card: blue reverse -->
  <g class="business-card card-reverse">
    <rect class="sheet-deep" x="12" y="233" width="80" height="55"/>
    <path d="M12 266 C35 254 60 280 92 262 L92 288 L12 288 Z" fill="var(--brand-blue)"/>
    <circle cx="21" cy="249" r="3.5" fill="var(--paper)"/>
    <text class="brand-name-light" x="27" y="250.5" font-size="4.6">bright harbor company</text>
  </g>

  <!-- Letterheads -->
  <g class="letterhead">
    <rect class="sheet" x="101" y="24" width="139" height="257"/>
    <circle class="brand-mark" cx="112" cy="40" r="4.5"/>
    <text class="brand-name" x="119" y="41.8" font-size="4.6">bright harbor company</text>
    <text class="contact-right" x="234" y="35">Street Name, District</text>
    <text class="contact-right" x="234" y="39">City, Country</text>
    <text class="contact-right" x="234" y="43">Postal Box Number</text>
    <text class="contact-right" x="234" y="47">Web Address</text>
    <circle class="faint-mark" cx="170" cy="150" r="34"/>
    <path class="wave-band" d="M101 256 C140 236 190 272 240 246 L240 281 L101 281 Z"/>
    <path class="wave-line" d="M101 252 C140 232 190 266 240 241"/>
  </g>

  <g class="letterhead">
    <rect class="sheet" x="266" y="24" width="139" height="257"/>
    <circle class="brand-mark" cx="277" cy="40" r="4.5"/>
    <text class="brand-name" x="284" y="41.8" font-size="4.6">bright harbor company</text>
    <text class="contact-right" x="399" y="35">Street Name, District</text>
    <text class="contact-right" x="399" y="39">City, Country</text>
    <text class="contact-right" x="399" y="43">Postal Box Number</text>
    <text class="contact-right" x="399" y="47">Web Address</text>
    <circle class="faint-mark" cx="335" cy="150" r="34"/>
    <path class="wave-band" d="M266 256 C305 236 355 272 405 246 L405 281 L266 281 Z"/>
    <path class="wave-line" d="M266 252 C305 232 355 266 405 241"/>
  </g>

  <!-- Compliment slips -->
  <g class="compliment-slip">
    <rect class="sheet" x="432" y="132" width="140" height="50"/>
    <circle class="brand-mark" cx="441" cy="142" r="3"/>
    <text class="brand-name" x="446" y="143.5" font-size="3.8">bright harbor company</text>
    <path class="wave-band" d="M432 170 C470 162 520 178 572 164 L572 182 L432 182 Z"/>
    <path class="wave-line" d="M432 167 C470 159 520 174 572 161"/>
  </g>

  <g class="compliment-slip">
    <rect class="sheet" x="432" y="204" width="140" height="50"/>
    <circle class="brand-mark" cx="441" cy="214" r="3"/>
    <text class="brand-name" x="446" y="215.5" font-size="3.8">bright harbor company</text>
    <path class="wave-band" d="M432 242 C470 234 520 250 572 236 L572 254 L432 254 Z"/>
    <path class="wave-line" d="M432 239 C470 231 520 246 572 233"/>
  </g>

  <!-- Envelopes -->
  <g class="envelope envelope-back">
    <rect class="sheet" x="948" y="62" width="200" height="58"/>
    <path class="envelope-grey" d="M948 62 L1148 62 L1148 68 L1048 96 L948 68 Z"/>
    <circle cx="1048" cy="74" r="3" fill="var(--paper)"/>
  </g>

  <g class="envelope envelope-open">
    <rect class="sheet" x="930" y="132" width="200" height="58"/>
    <path class="wave-band" d="M930 132 L1130 132 L1030 160 Z"/>
    <path class="flap-line" d="M930 190 L1030 156 L1130 190"/>
  </g>

  <g class="envelope envelope-front">
    <rect class="sheet" x="930" y="202" width="200" height="60"/>
    <path class="flap-line" d="M930 202 L1030 234 L1130 202"/>
    <path class="flap-line" d="M930 262 L1010 228 M1130 262 L1050 228"/>
  </g>

</svg>
</body>
</html>
```